Executive Business Consulting for Telco Companies and Telco Start up companies

1.) Looking for an appealing and action oriented business card design.
2.)The target companies to work with start-ups and existing companies that focus on Business to Business applications
3.) For "OKRA", a Belgium based Executive consultancy company specialised in global reach starting from the centre of Europe = Brussels.
4.) Our core competence is the Go To Market in All major global regions, incl North America, Latin America, Asia, Japan, Europe and Africa.
5.) Design should be appealing to CEO, CFO and Venture Funds signalling; Expertise, Stability, Maturity and Commitment
6.) Preferred color scheme is Blue focussed and using a modern FONT.
7.) Logo design is included (uploaded)

Target Market(s)

Telecommunication Market. Companies in a B2B business model, developping services or applications to make business run more profitable

Industry/Entity Type

Business

Contact Information for Business Card

Company Name: OKRA
Name: Joris Vandelay
Titel: Managing Director
Address: Kalkweg 58 , B-9170 Meerdonk , Belgium
Tel: + 32 471 208 364
Email: joris_vandelay@plimbox.example
LinkedIn: be.netprofilo.example/in/jorisvandelay/

Font styles to use
Serif

Colors
0455a3
3277b5

Requirements
Must have
• Second Side Text: Opening Key Regions Across the Globe

```html
<!DOCTYPE html>
<html lang="en">
<head>
<meta charset="utf-8">
<title>OKRA – Business Card</title>
<link rel="stylesheet" href="https://fonts.googleapis.com/css2?family=Maven+Pro:wght@400;500;600;800&display=swap">
<style>
  :root {
    --backdrop: #3b3b3d;
    --navy: #1b2a6b;
    --sky: #1e9ad6;
    --silver: #c9cacc;
    --paper: #ffffff;
    --ink: #1f2d6e;
  }
  * { box-sizing: border-box; margin: 0; padding: 0; }
  html, body { width: 1200px; height: 900px; overflow: hidden; }
  body {
    background: var(--backdrop);
    font-family: "Maven Pro", "Helvetica Neue", Arial, sans-serif;
    position: relative;
  }
  .card {
    position: absolute;
    top: 302px;
    width: 512px;
    height: 295px;
    border-radius: 18px;
    box-shadow: 0 4px 14px rgba(0,0,0,0.45);
    overflow: hidden;
  }
  /* Front side */
  .card-front { left: 73px; background: var(--navy); }
  .front-mark {
    position: absolute;
    left: 208px; top: 58px;
    width: 95px; height: 95px;
    border-radius: 50%;
    background: radial-gradient(circle at 40% 40%, #2f8fd6, #1b4f9c);
  }
  .front-name {
    position: absolute;
    left: 0; right: 0; top: 178px;
    text-align: center;
    font-weight: 800;
    font-size: 66px;
    letter-spacing: 2px;
    color: var(--silver);
    line-height: 1;
  }
  .front-tagline {
    position: absolute;
    left: 0; right: 0; top: 250px;
    text-align: center;
    font-size: 12.5px;
    color: var(--sky);
  }
  /* Back side */
  .card-back { left: 615px; background: var(--paper); }
  .back-brand {
    position: absolute;
    left: 29px; top: 37px;
    display: flex; align-items: center; gap: 18px;
  }
  .back-mark {
    width: 100px; height: 100px;
    border-radius: 50%;
    background: radial-gradient(circle at 40% 40%, #2f8fd6, #1b3f8c);
  }
  .back-name {
    font-weight: 800;
    font-size: 40px;
    letter-spacing: 1px;
    color: var(--navy);
  }
  .person {
    position: absolute;
    left: 245px; top: 136px;
    color: var(--ink);
  }
  .person-name { font-size: 19px; font-weight: 600; color: var(--sky); line-height: 1.2; }
  .person-title { font-size: 12.5px; margin-top: 4px; }
  .contacts { list-style: none; margin-top: 9px; font-size: 12.5px; line-height: 17.5px; }
  .contacts li { display: flex; align-items: flex-start; gap: 6px; }
  .contacts svg { flex: none; width: 11px; height: 11px; margin-top: 3px; fill: var(--sky); }
  .contacts .indent { padding-left: 17px; }
</style>
</head>
<body>
  <section class="card card-front">
    <div class="front-mark"></div>
    <div class="front-name">OKRA</div>
    <p class="front-tagline">Opening Key Regions Across the Globe</p>
  </section>

  <section class="card card-back">
    <div class="back-brand">
      <div class="back-mark"></div>
      <div class="back-name">OKRA</div>
    </div>
    <div class="person">
      <h1 class="person-name">Joris Vandelay</h1>
      <p class="person-title">Managing Director</p>
      <ul class="contacts">
        <li><svg viewBox="0 0 12 12" aria-hidden="true"><path d="M3 1 L5 3.5 L4 5 Q5 7 7 8 L8.5 7 L11 9 L9.5 11 Q4 10.5 1 3 Z"/></svg>+32 471 208 364</li>
        <li><svg viewBox="0 0 12 12" aria-hidden="true"><path d="M1 3 H11 V10 H1 Z M1.5 3.5 L6 7 L10.5 3.5" stroke="#fff" stroke-width="1"/></svg>joris_vandelay@plimbox.example</li>
        <li><svg viewBox="0 0 12 12" aria-hidden="true"><rect x="1" y="1" width="10" height="10" rx="1.5"/></svg>be.netprofilo.example/in/jorisvandelay/</li>
        <li><svg viewBox="0 0 12 12" aria-hidden="true"><path d="M6 0.5 A4 4 0 0 1 10 4.5 C10 7.5 6 11.5 6 11.5 C6 11.5 2 7.5 2 4.5 A4 4 0 0 1 6 0.5 Z M6 3 A1.5 1.5 0 1 0 6 6 A1.5 1.5 0 1 0 6 3 Z" fill-rule="evenodd"/></svg>Kalkweg 58, B-9170 Meerdonk</li>
        <li class="indent">Belgium</li>
      </ul>
    </div>
  </section>
</body>
</html>
```